GlowMoths Windows App design

We will need a designer to redesign our entire app for Windows Phone use.

Currently, we have apps available for Android and iOS, they can be downloaded here: http://www.travolink.example/downloads/

Other than just following the same concept, we want this app to be based on the Metro design, with an about page to tell user more about this app and our services, also to design the live tile.

Included are some designs done previously by other designers.
Updates

Dear Designers,

We would be making our decision based on the main screen, where device list is loaded. 

The main direction would be the metro style design.

Best Regards,
Berwin

Reason: We have pretty good designs in, just a few more days to see if there are any new entrants.

Industry/Entity Type

Android

```html
<!DOCTYPE html>
<html lang="en">
<head>
<meta charset="utf-8">
<title>GlowMoths – Devices</title>
<link rel="stylesheet" href="https://fonts.googleapis.com/css2?family=Open+Sans:wght@300;400&family=Roboto:wght@400&display=swap">
<style>
  :root {
    --bg-top: #4a4a4a;
    --bg-bottom: #1e1e1e;
    --panel: #000000;
    --text: #ffffff;
    --muted: #a8a8a8;
    --dim-title: #474747;
    --dim-text: #3c3c3c;
    --accent: #62d2cc;
    --status-warn: #e09a2e;
    --status-alert: #c4262b;
    --status-ok: #4b9b2e;
    --focus: #e5121a;
  }
  * { margin: 0; padding: 0; box-sizing: border-box; }
  html, body { width: 1200px; height: 960px; overflow: hidden; }
  body {
    background: radial-gradient(ellipse 900px 700px at 50% 0%, var(--bg-top), var(--bg-bottom));
    font-family: "Open Sans", sans-serif;
    color: var(--text);
  }
  .stage {
    position: relative;
    width: 1280px; height: 1024px;
    transform: scale(0.9375);
    transform-origin: 0 0;
  }
  .app-panel {
    position: absolute;
    left: 158px; top: 306px;
    width: 962px; height: 480px;
    background: var(--panel);
  }
  .brand {
    position: absolute;
    left: 14px; top: 16px;
    font-size: 27px; font-weight: 400;
    letter-spacing: 14px;
    color: var(--accent);
    line-height: 1;
  }
  .page-title {
    position: absolute;
    font-size: 30px; font-weight: 400;
    line-height: 1; top: 64px;
  }
  .devices { position: absolute; left: 12px; top: 0; width: 300px; height: 480px; }
  .devices .page-title { left: 0; color: var(--text); }
  .welcome {
    position: absolute; left: 0; top: 106px;
    font-size: 19px;
  }
  .welcome .user { color: var(--accent); }
  .device-list { position: absolute; left: 0; top: 144px; list-style: none; width: 272px; }
  .device {
    position: relative;
    height: 40px; margin-bottom: 10px;
    padding-left: 16px;
    border-left: 3px solid var(--status-ok);
  }
  .device.warn { border-left-color: var(--status-warn); }
  .device.alert { border-left-color: var(--status-alert); }
  .device-name { font-size: 19px; line-height: 22px; padding-top: 0; }
  .device-address {
    font-family: "Roboto", sans-serif;
    font-size: 12px; color: var(--muted);
    white-space: nowrap; overflow: hidden; text-overflow: ellipsis;
    width: 218px; line-height: 16px;
  }
  .device-open { position: absolute; right: 0; top: 5px; width: 30px; height: 30px; }
  .total {
    position: absolute; left: 0; top: 444px;
    font-size: 19px; color: var(--accent);
  }
  .about { position: absolute; left: 305px; top: 0; width: 290px; }
  .about .page-title, .logout .page-title { left: 0; color: var(--dim-title); font-weight: 300; }
  .dim-copy {
    position: absolute; left: 0; top: 107px;
    font-size: 15px; line-height: 19.3px; color: var(--dim-text);
    width: 282px;
  }
  .logout { position: absolute; left: 625px; top: 0; width: 250px; }
  .focus-frame {
    position: absolute;
    left: 158px; top: 305px;
    width: 324px; height: 483px;
    border: 2px solid var(--focus);
    pointer-events: none;
  }
</style>
</head>
<body>
<div class="stage">
  <main class="app-panel">
    <div class="brand">GLOWMOTHS</div>

    <section class="devices">
      <h1 class="page-title">devices</h1>
      <p class="welcome">Welcome, <span class="user">user876</span></p>
      <ul class="device-list">
        <li class="device warn">
          <div class="device-name">Device name</div>
          <div class="device-address">14 Harlow Quay Road 9, Meridian Bay</div>
          <svg class="device-open" viewBox="0 0 30 30" aria-hidden="true"><circle cx="15" cy="15" r="13" fill="none" stroke="#fff" stroke-width="2.6"/><path d="M8 15h13M15.5 9.5L21 15l-5.5 5.5" fill="none" stroke="#fff" stroke-width="2.6" stroke-linecap="round" stroke-linejoin="round"/></svg>
        </li>
        <li class="device warn">
          <div class="device-name">Device name</div>
          <div class="device-address">14 Harlow Quay Road 9, Meridian Bay</div>
          <svg class="device-open" viewBox="0 0 30 30" aria-hidden="true"><circle cx="15" cy="15" r="13" fill="none" stroke="#fff" stroke-width="2.6"/><path d="M8 15h13M15.5 9.5L21 15l-5.5 5.5" fill="none" stroke="#fff" stroke-width="2.6" stroke-linecap="round" stroke-linejoin="round"/></svg>
        </li>
        <li class="device alert">
          <div class="device-name">Device name</div>
          <div class="device-address">14 Harlow Quay Road 9, Meridian Bay</div>
          <svg class="device-open" viewBox="0 0 30 30" aria-hidden="true"><circle cx="15" cy="15" r="13" fill="none" stroke="#fff" stroke-width="2.6"/><path d="M8 15h13M15.5 9.5L21 15l-5.5 5.5" fill="none" stroke="#fff" stroke-width="2.6" stroke-linecap="round" stroke-linejoin="round"/></svg>
        </li>
        <li class="device alert">
          <div class="device-name">Device name</div>
          <div class="device-address">14 Harlow Quay Road 9, Meridian Bay</div>
          <svg class="device-open" viewBox="0 0 30 30" aria-hidden="true"><circle cx="15" cy="15" r="13" fill="none" stroke="#fff" stroke-width="2.6"/><path d="M8 15h13M15.5 9.5L21 15l-5.5 5.5" fill="none" stroke="#fff" stroke-width="2.6" stroke-linecap="round" stroke-linejoin="round"/></svg>
        </li>
        <li class="device">
          <div class="device-name">Device name</div>
          <div class="device-address">14 Harlow Quay Road 9, Meridian Bay</div>
          <svg class="device-open" viewBox="0 0 30 30" aria-hidden="true"><circle cx="15" cy="15" r="13" fill="none" stroke="#fff" stroke-width="2.6"/><path d="M8 15h13M15.5 9.5L21 15l-5.5 5.5" fill="none" stroke="#fff" stroke-width="2.6" stroke-linecap="round" stroke-linejoin="round"/></svg>
        </li>
        <li class="device">
          <div class="device-name">Device name</div>
          <div class="device-address">14 Harlow Quay Road 9, Meridian Bay</div>
          <svg class="device-open" viewBox="0 0 30 30" aria-hidden="true"><circle cx="15" cy="15" r="13" fill="none" stroke="#fff" stroke-width="2.6"/><path d="M8 15h13M15.5 9.5L21 15l-5.5 5.5" fill="none" stroke="#fff" stroke-width="2.6" stroke-linecap="round" stroke-linejoin="round"/></svg>
        </li>
      </ul>
      <p class="total">Total Device : 6 Devices</p>
    </section>

    <section class="about">
      <h2 class="page-title">about</h2>
      <p class="dim-copy">This is Pixelframe's version &nbsp;of Lorem Ipsum. Proin gravida nibh vel velit auctor aliquet. Aenean sollicitudin, lorem quis bibendum auctor, nisi elit consequat ipsum, nec sagittis sem nibh id elit. Duis sed odio sit amet nibh vulputate cursus a sit amet mauris. Morbi accumsan ipsum velit. Nam nec tellus a odio tincidunt auctor a ornare odio. Sed non &nbsp;mauris vitae erat consequat auctor eu in elit. Class aptent taciti sociosqu ad litora torquent per conubia nostra, per inceptos himenaeos. Mauris in erat justo. Nullam ac urna eu felis dapibus condimentum sit amet a augue. Sed non neque elit. Sed ut imperdiet nisi. Proin condimentum fermentum nunc. Etiam pharetra, erat sed fermentum feugiat,</p>
    </section>

    <section class="logout">
      <h2 class="page-title">logout</h2>
      <p class="dim-copy">Take care &amp; goodbye.</p>
    </section>
  </main>
  <div class="focus-frame"></div>
</div>
</body>
</html>
```